Modern & Aesthetic Electrician Sign Design for Work Vehicle

Modern and aesthetic signage design for an electricians work vehicle. Including already designed logo, mobile number, ABN, licensing number and services offered. Preference is black background, symmetric design with logo centred, services offered at bottom of sign in smaller size font. Mobile number readable and big enough to standout without being too large.

Industry/Entity Type

Electrician

Font styles to use
Serif
Sans Serif

Colors
000000
ffffff
ec1f27

Requirements
Must have
• Logo
• Services Offered
• Mobile Number
• ABN
• License Number
• Black background

```html
<!DOCTYPE html>
<html lang="en">
<head>
<meta charset="utf-8">
<title>Volton Electrical – Vehicle Signage</title>
<link rel="stylesheet" href="https://fonts.googleapis.com/css2?family=Roboto+Condensed:wght@400;700&display=swap">
<style>
  :root {
    --black: #000000;
    --white: #ffffff;
    --red: #ec1f27;
    --grey: #8f8f8f;
    --page: #ffffff;
    --label: #222222;
    --copper: #c9773f;
    --wire-green: #3fa64a;
    --wire-blue: #5b7fa8;
    --wire-red: #8a1f2a;
  }
  * { box-sizing: border-box; margin: 0; padding: 0; }
  html, body {
    width: 1200px; height: 800px; overflow: hidden;
    background: var(--page);
    font-family: "Roboto Condensed", "Arial Narrow", sans-serif;
  }
  .sheet { position: relative; width: 1200px; height: 800px; }

  .panel { position: absolute; background: var(--black); overflow: hidden; }
  .panel-label {
    position: absolute; font-size: 20px; color: var(--label); font-weight: 400;
  }

  /* Back panel */
  .back-panel { left: 12px; top: 30px; width: 775px; height: 305px; }
  .back-label { left: 12px; top: 340px; }

  .back-panel .call-us {
    position: absolute; left: 44px; top: 14px;
    font-size: 60px; font-weight: 700; color: var(--red); line-height: 1;
  }
  .back-panel .phone {
    position: absolute; left: 42px; top: 78px;
    font-size: 82px; font-weight: 400; color: var(--white); line-height: 1; letter-spacing: 1px;
  }
  .back-panel .wire-photo {
    position: absolute; left: 124px; top: 154px; width: 264px; height: 151px;
    background: radial-gradient(ellipse at 55% 40%, var(--copper) 0%, rgba(201,119,63,.5) 30%, transparent 60%),
                linear-gradient(120deg, var(--wire-green) 0%, var(--wire-blue) 45%, var(--wire-red) 70%, transparent 90%);
    border-radius: 50% 50% 0 0 / 60% 60% 0 0;
  }
  .back-panel .brand-dot {
    position: absolute; left: 556px; top: 57px; width: 146px; height: 146px;
    border: 6px solid var(--grey); border-radius: 50%;
  }
  .back-panel .brand-name {
    position: absolute; left: 506px; top: 222px; width: 258px; text-align: center;
    font-size: 31px; font-weight: 700; color: var(--red); line-height: 1; white-space: nowrap;
  }

  /* Side panel */
  .side-panel { left: 360px; top: 440px; width: 812px; height: 260px; }
  .side-label { left: 366px; top: 715px; }

  .side-panel .abn { position: absolute; left: 114px; top: 84px; line-height: 1.1; }
  .side-panel .abn-title { font-size: 11px; color: var(--red); font-weight: 400; }
  .side-panel .abn-number { font-size: 12px; color: var(--white); }

  .side-panel .brand-dot {
    position: absolute; left: 232px; top: 80px; width: 48px; height: 48px;
    border: 3px solid var(--grey); border-radius: 50%;
  }
  .side-panel .brand-name {
    position: absolute; left: 196px; top: 132px; width: 120px; text-align: center;
    font-size: 15px; font-weight: 700; color: var(--red); line-height: 1; white-space: nowrap;
  }
  .side-panel .services {
    position: absolute; left: 196px; top: 154px; width: 120px; text-align: center;
    font-size: 13px; color: var(--white); white-space: nowrap;
  }
  .side-panel .wire-photo {
    position: absolute; left: 312px; top: 120px; width: 100px; height: 66px;
    background: radial-gradient(ellipse at 60% 30%, var(--copper) 0%, transparent 60%),
                linear-gradient(120deg, var(--wire-green) 0%, var(--wire-red) 60%, transparent 90%);
    border-radius: 50% 50% 0 0 / 60% 60% 0 0;
  }
  .side-panel .feature-graphic {
    position: absolute; left: 410px; top: 20px; width: 150px; height: 150px;
    border-radius: 50%;
    background: radial-gradient(circle at 55% 45%, rgba(236,31,39,.55) 0%, rgba(143,143,143,.55) 55%, rgba(143,143,143,.25) 100%);
  }
  .side-panel .call-us {
    position: absolute; left: 606px; top: 58px;
    font-size: 21px; font-weight: 700; color: var(--red); line-height: 1;
  }
  .side-panel .phone {
    position: absolute; left: 606px; top: 78px;
    font-size: 31px; color: var(--white); line-height: 1; white-space: nowrap;
  }
  .side-panel .license { position: absolute; left: 684px; top: 108px; line-height: 1.05; }
  .side-panel .license-title { font-size: 9px; color: var(--red); }
  .side-panel .license-number { font-size: 11px; color: var(--white); }
</style>
</head>
<body>
<main class="sheet">

  <section class="panel back-panel" aria-label="Back vehicle panel">
    <p class="call-us">Call Us!</p>
    <p class="phone">000 000 0000</p>
    <div class="wire-photo" role="img" aria-label="Photo of stripped electrical cable with copper strands"></div>
    <div class="brand-dot" aria-hidden="true"></div>
    <p class="brand-name">Volton Electrical</p>
  </section>
  <p class="panel-label back-label">Back design</p>

  <section class="panel side-panel" aria-label="Side vehicle panel">
    <div class="abn">
      <p class="abn-title">ABN</p>
      <p class="abn-number">00 000 000 000</p>
    </div>
    <div class="brand-dot" aria-hidden="true"></div>
    <p class="brand-name">Volton Electrical</p>
    <p class="services">Services Offered</p>
    <div class="wire-photo" role="img" aria-label="Photo of stripped electrical cable with copper strands"></div>
    <div class="feature-graphic" role="img" aria-label="Large brand graphic area in grey and red"></div>
    <p class="call-us">Call Us!</p>
    <p class="phone">000 000 0000</p>
    <div class="license">
      <p class="license-title">License Number</p>
      <p class="license-number">00 000 000 000</p>
    </div>
  </section>
  <p class="panel-label side-label">Side design</p>

</main>
</body>
</html>
```